KWT Contracting services . Building and maintenance services, optic fibre installation

Business cards and logo design.I need a logo that I can use on business cards ,workwear and on my vehicles. I would like the KWT to be the main or larger text and contracting services to be the smaller or less important text.I like monograms, modern designs and repeating patterns symbols. I am also a Gemini and my favourite number is 22 so if this can be any inspiration to help with the design. Am thinking of the using German flag colours as a his is my family’s heritage. And the other 2 main colours I wear is black and white.But any ideas are appreciated.I do not need a design that is trade specific but a design that could be used for any business.

Target Market(s)

General public

Contact Information for Business Card

KWT Contracting Services ( front of business card)

(Back of business card)
Milo Brackwood
0471539264
Maintenance services
Optic fibre and data installation

Logo Text

Logo can just be pattern or monogram or incorporate KWT . I like the gemini star sign and the number 22

Colors
ec1f27
000000
fbee3e
ffffff

Requirements
Must have
• Logo and KWT Contracting Services on the front of business card
Nice to have
• Possible use of German flag colours.
• Modern design.
• Design to be able to be used on black or white background as I want to put it on clothing

```html
<!DOCTYPE html>
<html lang="en">
<head>
<meta charset="utf-8">
<title>KWT Contracting Services – Business Cards</title>
<link rel="stylesheet" href="https://fonts.googleapis.com/css2?family=Montserrat:wght@400;500;700;800&display=swap">
<style>
  :root {
    --backdrop: #8c8c8c;
    --brand-red: #8e1b20;
    --brand-red-dark: #73141a;
    --brand-red-light: #a0262b;
    --paper: #ffffff;
    --ink-grey: #6a6a6a;
    --ink-soft: #8a8a8a;
  }
  * { box-sizing: border-box; margin: 0; padding: 0; }
  html, body {
    width: 1200px; height: 877px; overflow: hidden;
    background: var(--backdrop);
    font-family: "Montserrat", sans-serif;
  }
  .stage {
    position: relative; width: 1200px; height: 877px;
    display: flex; align-items: center; justify-content: center; gap: 44px;
  }
  .card {
    position: relative; width: 520px; height: 297px;
    box-shadow: 0 14px 30px rgba(0,0,0,.28);
    overflow: hidden;
  }

  /* Front */
  .card--front {
    background: linear-gradient(135deg, var(--brand-red-light) 0%, var(--brand-red) 45%, var(--brand-red-dark) 100%);
    color: var(--paper);
  }
  .front-logo {
    position: absolute; left: 0; right: 0; top: 92px;
    text-align: center; font-weight: 800; line-height: 1;
  }
  .front-logo .wordmark { display: block; font-size: 64px; letter-spacing: 2px; }
  .front-logo .tagline { display: block; font-size: 15px; letter-spacing: 2.5px; margin-top: 6px; text-transform: uppercase; }
  .front-web {
    position: absolute; left: 0; right: 0; bottom: 22px;
    text-align: center; font-size: 9px; letter-spacing: 1.5px; font-weight: 500;
  }

  /* Back */
  .card--back { background: var(--paper); }
  .back-logo {
    position: absolute; left: 52px; top: 28px;
    color: var(--brand-red); font-weight: 800; line-height: 1;
  }
  .back-logo .wordmark { display: block; font-size: 40px; letter-spacing: 1px; }
  .back-logo .tagline { display: block; font-size: 9.5px; letter-spacing: 1.6px; margin-top: 3px; text-transform: uppercase; }
  .accent-tab {
    position: absolute; left: 0; top: 96px; width: 12px; height: 22px;
    background: var(--brand-red);
  }
  .contact { position: absolute; left: 52px; top: 96px; }
  .contact-name { font-size: 16px; color: var(--brand-red); letter-spacing: .5px; }
  .contact-name strong { font-weight: 700; }
  .contact-name span { font-weight: 400; }
  .contact-role { font-size: 8.5px; color: var(--ink-grey); margin-top: 2px; }
  .contact-label { font-size: 8.5px; color: var(--brand-red); margin-top: 14px; }
  .contact-line { font-size: 8.5px; color: var(--ink-soft); line-height: 1.45; }
  .rule {
    position: absolute; left: 240px; right: 0; top: 150px; height: 1px;
    background: var(--brand-red);
  }
  .services {
    position: absolute; right: 30px; bottom: 34px; list-style: none;
    text-align: right; font-size: 10.5px; color: var(--ink-grey); line-height: 1.6;
  }
  .services li::after {
    content: ""; display: inline-block; width: 5px; height: 5px; border-radius: 50%;
    background: var(--brand-red); margin-left: 7px; vertical-align: middle;
  }
  .edge-mark {
    position: absolute; right: 0; width: 10px; height: 2px; background: var(--brand-red);
  }
</style>
</head>
<body>
<main class="stage">
  <section class="card card--front" aria-label="Business card front">
    <div class="front-logo">
      <span class="wordmark">KWT</span>
      <span class="tagline">Contracting Services</span>
    </div>
    <p class="front-web">www.kwtcontractingservices.com</p>
  </section>

  <section class="card card--back" aria-label="Business card back">
    <div class="back-logo">
      <span class="wordmark">KWT</span>
      <span class="tagline">Contracting Services</span>
    </div>
    <div class="accent-tab"></div>
    <div class="contact">
      <p class="contact-name"><strong>MILO</strong> <span>BRACKWOOD</span></p>
      <p class="contact-role">General Manager</p>
      <p class="contact-label">info:</p>
      <p class="contact-line">0471539264</p>
      <p class="contact-line">milobrackwood@mail.com</p>
    </div>
    <div class="rule"></div>
    <ul class="services">
      <li>Maintenance services</li>
      <li>Optic fibre and data installation</li>
    </ul>
    <div class="edge-mark" style="bottom:48px"></div>
    <div class="edge-mark" style="bottom:38px"></div>
  </section>
</main>
</body>
</html>
```